Electrical Contractor Company Profile

We need a Brochure that is more entertaining than our current Company Profile Document. We have lots of great experience and awesome looking jobs in our portfolio but need a document that we can either print of send in electronic format to accompany some of our submissions.

We are ideally looking for something 9-10 pages in A4 with some of the pages opening out to A3.

We are looking for a document that is professional and smart however shows the colour and quality that we feel we offer to prospective clientele.

I have included the current Company Profile and Logo along with a number of images of completed projects that may be of use.

Target Market(s)

Builders, Facility Managers, Engineers, Decision makers

Industry/Entity Type

Electrical

Font styles to use
Sans Serif

Colors

Designer to choose colors to be used in the design.

Requirements
Must have
• - Modern look with a focus on sustainability
• - Clean Simple and Professional
• - Incorporate our Logo
• Core Business Lines need to be across an A3 opening page and have photos relating to these lines Solar, Communications and any of the projects.
Nice to have
• Lots of colour and photos mixed with the text
Should not have
• Lightning bolts or corny symbols

```html
<!DOCTYPE html>
<html lang="en">
<head>
<meta charset="utf-8">
<title>Clearline Electrical Services – Company Profile</title>
<link rel="stylesheet" href="https://fonts.googleapis.com/css2?family=Montserrat:wght@300;400;600;700;800&display=swap">
<style>
:root{
  --bg:#e4e4e4;
  --paper:#ffffff;
  --ink:#1e1e24;
  --title:#8d91ab;
  --title-dark:#6f7390;
  --quote-ink:#3a3a40;
  --lime:#c9d43a;
  --steel:#9aa3c2;
  --sun:#f2c84a;
  --sand:#c9b8a2;
  --fold:#d6d6d6;
}
*{box-sizing:border-box;margin:0;padding:0}
html,body{width:1200px;height:1200px;overflow:hidden}
body{background:var(--bg);font-family:"Montserrat",sans-serif;color:var(--ink)}
.spreads{position:absolute;left:60px;top:30px;width:1080px;display:flex;flex-direction:column;gap:18px}
.spread{display:grid;grid-template-columns:1fr 1fr;height:368px;background:var(--paper);box-shadow:0 3px 10px rgba(0,0,0,.18)}
.page{position:relative;padding:26px 30px;overflow:hidden}
.page--left{border-right:1px solid var(--fold)}
.photo{border-radius:1px}
.title{font-weight:800;font-size:25px;letter-spacing:.02em;color:var(--title);text-transform:uppercase;margin-bottom:18px}
.h{font-weight:700;font-size:7.5px;letter-spacing:.14em;text-transform:uppercase;margin:0 0 6px}
.lead{font-weight:700;font-size:7.5px;line-height:1.4;margin-bottom:9px}
p,li{font-size:7.3px;line-height:1.45}
ul{list-style:none}
li{position:relative;padding-left:8px;margin-bottom:5px}
li::before{content:"›";position:absolute;left:0;top:0}
.quote{position:relative;padding-left:22px}
.quote__mark{position:absolute;left:0;top:-26px;font-size:120px;line-height:1;font-weight:800;opacity:.85}
.quote__text{position:relative;font-weight:400;font-size:13.5px;line-height:1.55;color:var(--quote-ink)}
.quote__by{position:relative;font-size:7.5px;font-style:italic;text-align:right;margin-top:6px}
.cols{display:grid;grid-template-columns:1fr 1fr;gap:26px}
/* spread 1 */
.s1-photo{height:220px;background:linear-gradient(180deg,#e8edf2 0%,#c7ccd3 40%,#6f7d5e 78%,#5d7a3c 100%)}
.s1 .quote{margin-top:26px}
.s1 .quote__mark{color:var(--lime)}
.solar-small{position:absolute;right:30px;bottom:18px;width:245px;height:155px;background:linear-gradient(180deg,#dfe8ef 0%,#b6c7d4 25%,#3a4f8f 60%,#223574 100%)}
.env-sub{display:grid;grid-template-columns:1fr 1fr;gap:10px}
/* spread 2 */
.core-grid{display:grid;grid-template-columns:repeat(3,1fr);column-gap:18px;row-gap:26px}
.core-grid p{font-size:7px}
.s2 .quote{margin-top:6px}
.s2 .quote__mark{color:var(--steel)}
.s2 .quote__text{font-size:12.5px}
.solar-big{margin-top:14px;height:250px;background:linear-gradient(180deg,#e6ebef 0%,#c9d3dc 22%,#3d55a0 55%,#1f2e6b 100%)}
/* spread 3 */
.s3-photo{height:230px;background:linear-gradient(180deg,#f2b227 0%,#c9c6c2 35%,#8e7e70 60%,#a0462e 100%)}
.s3 .page--left .quote{margin-top:28px}
.s3 .page--left .quote__mark{color:var(--sun)}
.pms{display:grid;grid-template-columns:1fr 205px;gap:22px}
.pms .title{font-size:23px;color:#a9a6a6}
.switch-photo{height:170px;background:linear-gradient(90deg,#e86a1c 0%,#f08a2c 35%,#7d7d82 55%,#e2662a 100%)}
.s3 .page--right .quote{margin-top:14px}
.s3 .page--right .quote__mark{color:var(--sand);top:-10px}
.s3 .page--right .quote__text{font-size:12px;text-align:right}
.mini-cols{display:grid;grid-template-columns:1fr 1fr;gap:14px;margin-bottom:10px}
</style>
</head>
<body>
<main class="spreads">

  <section class="spread s1">
    <div class="page page--left">
      <div class="photo s1-photo" role="img" aria-label="Photo of a modern sports centre building with curved white facade and entry sign"></div>
      <blockquote class="quote">
        <span class="quote__mark">“</span>
        <p class="quote__text">The finished product at the Harbourside Sports Centre was of excellent quality. We were extremely impressed with the ease of use and high levels of communication we received.”</p>
        <p class="quote__by">Mark Tollard, Brennan Builders</p>
      </blockquote>
    </div>
    <div class="page page--right">
      <h2 class="title">Safety &amp; Environment</h2>
      <div class="cols">
        <div>
          <h3 class="h">Health and Safety</h3>
          <p style="margin-bottom:8px">Clearline Electrical Services utilises a comprehensive HSEQ Management System, which has been developed by the State Contractors Guild and tailored to suit the business.</p>
          <p class="lead">Our high level of safety is achieved by:</p>
          <ul>
            <li>Planning, developing, implementing and monitoring comprehensive health, safety and welfare programs</li>
            <li>Promoting the understanding of health, safety and welfare as a normal component of all aspects of work. Developing site specific systems and plans to meet the requirements of each project</li>
            <li>Ensuring staff receive appropriate safety and first aid training</li>
            <li>Providing a healthy and safe workplace</li>
          </ul>
          <h3 class="h" style="margin-top:8px">The System:</h3>
          <ul>
            <li>Certified to the QHSE Code 2013</li>
            <li>Fully meets the requirements of AS/NZS 4801:2001 – OHS Management Systems</li>
            <li>Our system is audited twice annually to ensure that the system is being utilised</li>
          </ul>
        </div>
        <div>
          <h3 class="h">Environment</h3>
          <p class="lead">Clearline Electrical Services works to deliver all projects in an environmentally responsible manner.</p>
          <div class="env-sub">
            <p>We have a comprehensive set of policies and procedures that ensure we comply with all relevant environmental legislation, regulations, codes of practice and contractual conditions.</p>
            <p>We also conduct business with suppliers and sub-contractors who have a commitment to responsible environmental management.</p>
          </div>
        </div>
      </div>
      <div class="photo solar-small" role="img" aria-label="Photo of rooftop solar panel rows under a blue sky"></div>
    </div>
  </section>

  <section class="spread s2">
    <div class="page page--left">
      <h2 class="title" style="margin-top:10px">Core Business</h2>
      <p class="lead" style="margin-bottom:16px">Clearline Electrical Services maintains six core lines of business:</p>
      <div class="core-grid">
        <div>
          <h3 class="h">Breakdown and Response</h3>
          <p>Providing a 24/7 call out service to a number of high profile clients this team is high energy and responsive to most situations. Consistently performing at the top level of our clients expectations have resulted in excellent growth in this sector.</p>
        </div>
        <div>
          <h3 class="h">Electrical Projects</h3>
          <p>This line of business is responsible for completing contracts both considered minor and major in value. Team members are experienced in installing various types of electrical systems and are well equipped in producing the high quality workmanship expected in this highly competitive sector.</p>
        </div>
        <div>
          <h3 class="h">Solar PV</h3>
          <p>Focusing on the commercial market, we are able to offer fully-design solutions for photovoltaic systems up to 200KW to suit a client's needs and budgets. With highly trained and experienced consultants and installers, we pride ourselves on offering great value and clarity on project benefits.</p>
        </div>
        <div>
          <h3 class="h">Planned Maintenance</h3>
          <p>This team services over 500 sites across the metropolitan area. Carrying out planned testing and repair of all electrical infrastructure required by our clients. This includes RCD and Emergency lighting along with thermographic surveys amongst many other services.</p>
        </div>
        <div>
          <h3 class="h">Communications</h3>
          <p>Our staff is extremely experienced. The majority of personnel carry Open Cabling licenses &amp; Certificate III qualifications in Telecommunications. The company owns substantial amounts of specialized test equipment and regularly invests in continued staff training. CES can supply both design and installation services for private networks, providing a certified solution to any copper and fiber optic needs.</p>
        </div>
        <div>
          <h3 class="h">Technology Services</h3>
          <p>With great base knowledge and an ongoing commitment to training and innovation, CES is able to offer solutions for Energy Management, Energy Conservation, Electronic Lighting Control, Premise's performance auditing and Power monitoring. Providing our clients with valuable expertise in reducing running costs and better understand their assets maintenance requirements, producing ongoing savings in operation and replacement of plant.</p>
        </div>
      </div>
    </div>
    <div class="page page--right">
      <blockquote class="quote">
        <span class="quote__mark">“</span>
        <p class="quote__text">We have a long history on various projects and have been extremely satisfied with the levels of quality and customer service we have received.”</p>
        <p class="quote__by">Paul Varga, Northline Construction</p>
      </blockquote>
      <div class="photo solar-big" role="img" aria-label="Photo of long rows of solar panels across a large industrial roof"></div>
    </div>
  </section>

  <section class="spread s3">
    <div class="page page--left">
      <div class="photo s3-photo" role="img" aria-label="Photo of a brewery restaurant interior with steel brewing tanks, pendant lights and brick walls"></div>
      <blockquote class="quote">
        <span class="quote__mark">“</span>
        <p class="quote__text">The final quality of workmanship on Riverbend is a reflection of the commitment that Clearline Electrical applies to all its projects.”</p>
        <p class="quote__by">Paul Varga, Northline Construction</p>
      </blockquote>
    </div>
    <div class="page page--right">
      <h2 class="title">Proven Management Systems</h2>
      <div class="pms">
        <div>
          <p class="lead">Our commitment to quality, health and safety and the environment places Clearline Electrical Services apart from our many competitors.</p>
          <div class="mini-cols">
            <p>Clearline Electrical Services is committed to providing clients with exceptional products and services in a creative and innovative manner.</p>
            <p>With our Integrated Management system aligned to ISO9001:2008 we ensure a consistent result is achieved in all cases.</p>
          </div>
          <h3 class="h">Our Quality System Ensures:</h3>
          <div class="mini-cols">
            <ul>
              <li>Consistent communication with all stakeholders</li>
              <li>Experienced and qualified staff are employed who are committed to company vision and commitment to quality</li>
              <li>Flexible workforce whereby staff are able to work across all lines of business</li>
            </ul>
            <ul>
              <li>Internal systems and software that allow thorough reporting and auditing</li>
              <li>Clearly defined roles and responsibilities for all staff</li>
              <li>Correct staff training and support</li>
              <li>Quality monitoring and reporting throughout the entire process</li>
            </ul>
          </div>
        </div>
        <div>
          <div class="photo switch-photo" role="img" aria-label="Photo of orange electrical switchboards and control panels"></div>
          <blockquote class="quote">
            <span class="quote__mark">“</span>
            <p class="quote__text">The finished product is of excellent quality, and we have been extremely impressed with the ease of use and high levels of communication received.”</p>
            <p class="quote__by">Glen Harper, Westgate Tower</p>
          </blockquote>
        </div>
      </div>
    </div>
  </section>

</main>
</body>
</html>
```